Modern Real Estate Sign For Realtor

We need to real estate sign 24x36 or (24x30 if it fits better) Sign that will be attached to a post at homes that are for sale. I like the style of the Meridian 40 yard signs I attached and PD sign with the white trim around it. I Also attached my business card with my logo and name. I would like a black sign with white writing.  I would also like to see options with my headshot included on the sign, either centered or on the right side. The following text should go on the sign:
Logo at the top.
Marcus Hollet
555.317.2096
Marcus@MHolletHomes.example

Requirements
Must have
- Logo at the top.
- Marcus Hollet
- 555.317.2096
- Marcus@MHolletHomes.example

Nice to have
- Headshot open to different design options for how it will be placed on the sign.
- MHolletHomes.example

```html
<!DOCTYPE html>
<html lang="en">
<head>
<meta charset="UTF-8">
<title>Hollet Homes Yard Sign</title>
<link rel="stylesheet" href="https://fonts.googleapis.com/css2?family=Montserrat:wght@500;600&display=swap">
<style>
  :root {
    --sign-black: #000000;
    --sign-white: #ffffff;
    --backdrop: #e9e6e0;
    --photo-top: #7d9a62;
    --photo-mid: #b8ad98;
    --photo-low: #5e6066;
  }
  html, body {
    margin: 0;
    padding: 0;
    width: 784px;
    height: 1200px;
    overflow: hidden;
    background: var(--backdrop);
  }
  .yard-sign {
    position: absolute;
    left: 12px;
    top: 30px;
    width: 760px;
    height: 1140px;
    background: var(--sign-black);
    color: var(--sign-white);
    overflow: hidden;
  }
  .brand {
    position: absolute;
    left: 0;
    right: 0;
    top: 120px;
    text-align: center;
  }
  .brand-name {
    font-family: "Montserrat", sans-serif;
    font-weight: 500;
    font-size: 60px;
    letter-spacing: 4px;
    line-height: 1;
    margin: 0;
    text-transform: uppercase;
  }
  .headshot {
    position: absolute;
    left: 0;
    top: 245px;
    width: 480px;
    height: 520px;
  }
  .agent-name {
    position: absolute;
    left: 296px;
    top: 428px;
    width: 434px;
    height: 80px;
    background: var(--sign-black);
    font-family: "Montserrat", sans-serif;
    font-weight: 600;
    font-size: 46px;
    line-height: 80px;
    text-align: right;
    margin: 0;
    text-transform: uppercase;
    white-space: nowrap;
  }
  .phone {
    position: absolute;
    left: 0;
    right: 0;
    top: 790px;
    text-align: center;
    font-family: "Montserrat", sans-serif;
    font-weight: 500;
    font-size: 88px;
    letter-spacing: 1px;
    line-height: 1;
  }
  .contact-list {
    position: absolute;
    left: 0;
    right: 0;
    top: 955px;
    margin: 0;
    padding: 0;
    list-style: none;
    text-align: center;
    font-family: "Montserrat", sans-serif;
    font-weight: 500;
    font-size: 31px;
    line-height: 50px;
  }
  .contact-list svg {
    width: 26px;
    height: 26px;
    vertical-align: -3px;
    margin-right: 10px;
  }
</style>
</head>
<body>
  <main class="yard-sign">
    <header class="brand">
      <h1 class="brand-name">Hollet Homes</h1>
    </header>

    <svg class="headshot" viewBox="0 0 480 520" xmlns="http://www.w3.org/2000/svg">
      <defs>
        <linearGradient id="portrait-tones" x1="0" y1="0" x2="0" y2="1">
          <stop offset="0" stop-color="var(--photo-top)"/>
          <stop offset="0.5" stop-color="var(--photo-mid)"/>
          <stop offset="1" stop-color="var(--photo-low)"/>
        </linearGradient>
      </defs>
      <polygon points="0,0 395,-10 408,480 0,500" fill="var(--sign-white)"/>
      <polyline points="400,-8 430,5 440,470 420,478" fill="none" stroke="var(--sign-white)" stroke-width="3"/>
      <polyline points="410,490 30,515" fill="none" stroke="var(--sign-white)" stroke-width="3"/>
      <rect x="18" y="30" width="372" height="380" fill="url(#portrait-tones)" role="img" aria-label="Headshot of the agent outdoors"/>
    </svg>

    <h2 class="agent-name">Marcus Hollet</h2>

    <div class="phone">555.317.2096</div>

    <ul class="contact-list">
      <li>
        <svg viewBox="0 0 24 24" aria-hidden="true"><rect x="2" y="5" width="20" height="14" fill="none" stroke="currentColor" stroke-width="2"/><polyline points="2,5 12,13 22,5" fill="none" stroke="currentColor" stroke-width="2"/></svg>Marcus@MHolletHomes.example
      </li>
      <li>
        <svg viewBox="0 0 24 24" aria-hidden="true"><circle cx="12" cy="12" r="10" fill="currentColor"/><ellipse cx="12" cy="12" rx="4" ry="10" fill="none" stroke="#000" stroke-width="1.5"/><line x1="2" y1="12" x2="22" y2="12" stroke="#000" stroke-width="1.5"/></svg>MHolletHomes.example
      </li>
    </ul>
  </main>
</body>
</html>
```